Lucid Haven - Need Stationary Design

We need a stationary pack for our new Care company based in the uk
Are corporate colours are Pink and purple
Please use attached logo
Target Market(s)
The Care Industry
Industry/Entity Type
It Company
Contact Information for Business Card
Moira Blythe
Director

```html
<!DOCTYPE html>
<html lang="en">
<head>
<meta charset="utf-8">
<title>Lucid Haven – Stationery Pack</title>
<link href="https://fonts.googleapis.com/css2?family=Open+Sans:wght@400;600;700&display=swap" rel="stylesheet">
<style>
  :root{
    --board:#d7dadd;
    --pink:#e2449a;
    --purple:#8b5ca8;
    --grey:#8a8a8a;
    --ink:#333;
    --paper:#ffffff;
    --rule:#e6e6e6;
    --cell:#ececec;
  }
  *{box-sizing:border-box;margin:0;padding:0}
  html,body{width:1200px;height:737px;overflow:hidden;background:var(--board)}
  body{font-family:"Open Sans",Arial,sans-serif;color:var(--ink)}
  .board{position:relative;width:1200px;height:737px;overflow:hidden}
  .abs{position:absolute}
  .label{position:absolute;font-size:7px;color:#333}
  .sheet{position:absolute;background:var(--paper);box-shadow:0 1px 3px rgba(0,0,0,.25);overflow:hidden}

  .logo{display:inline-flex;align-items:center;gap:.35em;white-space:nowrap;font-weight:400;color:var(--purple)}
  .logo .dot{width:.7em;height:.7em;border-radius:50%;background:var(--pink);flex:none}
  .logo.grey{color:var(--grey)} .logo.grey .dot{background:var(--grey)}
  .logo.white{color:#fff} .logo.white .dot{background:#fff}
  .logo.pink{color:var(--pink)} .logo.pink .dot{background:var(--purple)}

  .band{position:absolute;left:0;right:0;bottom:0;display:flex;color:#fff}
  .band .seg-pink{background:var(--pink)}
  .band .seg-purple{background:var(--purple)}
  .band span{display:flex;align-items:center;justify-content:center}

  /* Letterhead */
  .letterhead{left:28px;top:86px;width:256px;height:330px}
  .letterhead .logo{position:absolute;left:0;right:0;top:28px;justify-content:center;font-size:8px}
  .letter-body{position:absolute;left:20px;top:68px;width:215px;font-size:4.3px;line-height:1.35}
  .letter-body p{margin-bottom:4px}
  .letter-body .strong{font-weight:700}
  .signature{width:55px;height:16px;margin:4px 0 1px;background:linear-gradient(90deg,#cfcfcf,#eee)}
  .letterhead .band{height:19px;font-size:4px}

  /* Fax */
  .fax{left:324px;top:86px;width:255px;height:331px}
  .fax .logo{position:absolute;left:22px;top:52px;font-size:8.5px}
  .fax-contact{position:absolute;left:173px;top:18px;font-size:3.6px;line-height:1.45}
  .fax-contact i{display:inline-block;width:3px;height:3px;background:var(--purple);margin-right:2px;vertical-align:middle}
  .fax-table{position:absolute;left:8px;top:73px;width:240px;border-collapse:separate;border-spacing:1px;font-size:3.8px}
  .fax-table td{height:11px;padding-left:4px}
  .fax-table td.k{background:var(--cell);width:32px}
  .fax-table td.v{background:#f2f2f2;width:84px}
  .fax-checks{position:absolute;left:8px;top:136px;width:240px;display:flex;justify-content:space-between;font-size:3.6px}
  .fax-checks span::before{content:"";display:inline-block;width:4px;height:4px;border:.5px solid #555;margin-right:2px;vertical-align:middle}
  .fax-comments{position:absolute;left:8px;top:148px;font-size:3.8px}
  .fax .band{height:7px}

  /* Folder */
  .folder{left:631px;top:42px;width:541px;height:486px}
  .folder-tree{left:676px;top:132px;width:144px;height:204px;border-radius:45% 45% 30% 30%;
    background:radial-gradient(ellipse at 50% 40%,rgba(255,255,255,.32),rgba(255,255,255,.08) 70%,rgba(255,255,255,0) 72%)}
  .folder-contact{left:650px;top:349px;font-size:4.4px;line-height:1.35;color:#fff}
  .folder-logo{left:972px;top:228px;font-size:19px}

  /* Envelopes */
  .envelope{left:30px;top:450px;width:286px;height:124px}
  .envelope .logo{position:absolute;left:13px;top:30px;font-size:7.5px}
  .envelope-mark{left:142px;top:10px;width:92px;height:104px;border-radius:45%;
    background:radial-gradient(ellipse,rgba(139,92,168,.14),rgba(226,68,154,.06) 60%,rgba(255,255,255,0) 72%)}
  .envelope .band{height:10px;font-size:3.8px}
  .envelope-back{left:328px;top:450px;width:285px;height:124px}
  .envelope-back .logo{position:absolute;left:0;right:0;top:10px;justify-content:center;font-size:5px}

  /* Business cards */
  .card{width:165px;height:93px}
  .card-one{left:26px;top:618px}
  .card-one .logo{position:absolute;left:7px;top:52px;font-size:7.5px}
  .card-one .details{position:absolute;right:7px;top:6px;text-align:right;color:#fff;font-size:5.2px;line-height:1.3}
  .card-one .name{font-weight:700;font-size:6.5px}
  .card-two{left:210px;top:617px}
  .card-two .who{position:absolute;left:7px;top:6px;font-size:6.5px;font-weight:700;line-height:1.1}
  .card-two .who small{display:block;font-weight:400;font-size:5px;color:#555}
  .card-two .logo{position:absolute;left:0;right:0;top:40px;justify-content:center;font-size:7.5px}
  .card-two .contacts{position:absolute;left:28px;top:67px;display:grid;grid-template-columns:auto auto;column-gap:10px;font-size:5px;line-height:1.3}
  .card-two .contacts i{display:inline-block;width:5px;height:5px;border-radius:50%;background:var(--pink);margin-right:2px;vertical-align:-1px}
  .card-two .band{height:8px;font-size:4px}
  .card-black{left:398px;top:616px;background:#000}
  .card-white{left:580px;top:614px}
  .card-black .logo,.card-white .logo{position:absolute;left:0;right:0;top:40px;justify-content:center;font-size:10px}

  /* CD */
  .cd{left:759px;top:568px;width:140px;height:140px}
  .cd-label{left:759px;top:660px;width:140px;text-align:center}
  .cd-label .logo{font-size:7px}

  /* CD cover */
  .cd-cover{left:914px;top:556px;width:200px;height:170px;background:transparent;box-shadow:none}
  .cd-cover .tab{position:absolute;left:0;top:0;width:200px;height:27px;background:var(--pink);border-radius:8px 8px 0 0}
  .cd-cover .body{position:absolute;left:0;top:27px;width:200px;height:143px;background:var(--paper);box-shadow:0 1px 3px rgba(0,0,0,.25)}
  .cd-cover .logo{position:absolute;left:0;right:0;top:103px;justify-content:center;font-size:14px}
  .cd-cover .band{height:9px}
</style>
</head>
<body>
<div class="board">

  <div class="abs" style="left:184px;top:28px"><span class="logo grey" style="font-size:22px"><span class="dot"></span>Lucid Haven</span></div>

  <!-- Letterhead -->
  <div class="label" style="left:30px;top:70px">Letter Head</div>
  <section class="sheet letterhead">
    <span class="logo"><span class="dot"></span>Lucid Haven</span>
    <div class="letter-body">
      <p>Date</p>
      <p class="strong">Recipient Name</p>
      <p>Company Name<br>Street Address<br>City, State, Zip</p>
      <p style="margin-top:10px">Thank you for choosing our care team. We are writing to confirm the details of your upcoming visit and to share a short overview of the support we will provide during the first weeks. Our staff will arrive at the agreed time and stay in touch with your family throughout.</p>
      <p>Each care plan is shaped around the person receiving it. Before the first visit a coordinator will meet with you to talk about daily routines, medication, meals, mobility and the small things that matter most. We review every plan at regular intervals and adjust it whenever your needs change, so the support always fits the life you want to lead at home.</p>
      <p>If you have any questions before we begin, please contact our office by phone or email. A member of the team is available every day of the week and will be glad to help. We look forward to working with you and your family in the months ahead.</p>
      <p style="margin-top:10px;margin-bottom:0">Sincerely,</p>
      <div class="signature" role="img" aria-label="Handwritten signature"></div>
      <p style="margin:0 0 0 16px">John Doe<br>Title</p>
    </div>
    <div class="band">
      <span class="seg-pink" style="width:62%">1234 Central Ave, Your City, ST 45608</span>
      <span class="seg-purple" style="width:38%">000-000-0000 &nbsp;|&nbsp; 000-000-0000 &nbsp;&nbsp; www.yourwebsite.com</span>
    </div>
  </section>

  <!-- Fax -->
  <div class="label" style="left:330px;top:74px">Fax</div>
  <section class="sheet fax">
    <span class="logo"><span class="dot"></span>Lucid Haven</span>
    <div class="fax-contact">1234 Central Ave<br>Your City, ST 45608<br><i></i>000-000-0000<br><i></i>000-000-0000<br><i></i>mail@yourwebsite.com<br><i></i>www.yourwebsite.com</div>
    <table class="fax-table">
      <tr><td class="k">To</td><td class="v"></td><td class="k">From</td><td class="v"></td></tr>
      <tr><td class="k">Fax</td><td class="v"></td><td class="k">Pages</td><td class="v"></td></tr>
      <tr><td class="k">Phone</td><td class="v"></td><td class="k">Date</td><td class="v"></td></tr>
      <tr><td class="k">Re</td><td class="v"></td><td class="k">CC</td><td class="v"></td></tr>
    </table>
    <div class="fax-checks"><span>Urgent</span><span>For Review</span><span>Please comment</span><span>Please reply</span><span>Please recycle</span></div>
    <div class="fax-comments">Comments :</div>
    <div class="band"><span class="seg-pink" style="width:50%"></span><span class="seg-purple" style="width:50%"></span></div>
  </section>

  <!-- Folder -->
  <div class="label" style="left:631px;top:25px">Folder</div>
  <svg class="abs folder" viewBox="0 0 541 486" aria-hidden="true">
    <rect x="0" y="0" width="270" height="486" fill="var(--pink)"/>
    <path d="M0 358 H262 L270 486" fill="none" stroke="#d03a8b" stroke-width="1"/>
    <rect x="271" y="0" width="270" height="350" fill="#fff"/>
    <rect x="271" y="350" width="135" height="8" fill="var(--pink)"/>
    <rect x="406" y="350" width="135" height="8" fill="var(--purple)"/>
    <polygon points="271,358 541,358 541,486 277,486" fill="var(--pink)"/>
  </svg>
  <div class="abs folder-tree" role="img" aria-label="Large faint tree decoration"></div>
  <div class="abs folder-contact">1234 Central Ave<br>Your City, ST 45608<br><br>000-000-0000<br>000-000-0000<br>www.yourwebsite.com</div>
  <div class="abs folder-logo"><span class="logo"><span class="dot"></span>Lucid Haven</span></div>

  <!-- Envelope -->
  <div class="label" style="left:32px;top:438px">Envelope</div>
  <section class="sheet envelope">
    <span class="logo"><span class="dot"></span>Lucid Haven</span>
    <div class="abs envelope-mark" role="img" aria-label="Faint tree decoration"></div>
    <div class="band">
      <span class="seg-pink" style="width:104px">1234 Central Ave, Your City, ST 45608</span>
      <span class="seg-purple" style="flex:1">www.yourwebsite.com</span>
    </div>
  </section>

  <div class="label" style="left:336px;top:438px">Envelope-Back</div>
  <section class="sheet envelope-back">
    <svg class="abs" style="left:0;top:0" width="285" height="30" aria-hidden="true">
      <polygon points="0,2 285,2 280,28 6,28" fill="var(--pink)"/>
    </svg>
    <span class="logo white"><span class="dot"></span>Lucid Haven</span>
  </section>

  <!-- Business cards -->
  <div class="label" style="left:36px;top:601px">Business Card_Option 1</div>
  <section class="sheet card card-one">
    <svg class="abs" style="left:0;top:0" width="165" height="93" aria-hidden="true">
      <path d="M66 93 C92 62 98 12 124 0 H165 V93 Z" fill="var(--pink)"/>
      <path d="M60 93 C88 62 94 12 120 0" fill="none" stroke="var(--purple)" stroke-width="1.2"/>
    </svg>
    <span class="logo"><span class="dot"></span>Lucid Haven</span>
    <div class="details">
      <div class="name">YOUR NAME</div>Title<br><br>
      1234 Central Ave<br>Your City, ST 45608<br><br>
      000-000-0000<br>000-000-0000<br>000-000-0000<br>mail@yourwebsite.com<br>www.yourwebsite.com
    </div>
  </section>

  <div class="label" style="left:219px;top:603px">Business Card_Option 2</div>
  <section class="sheet card card-two">
    <div class="who">YOUR NAME<small>Title</small></div>
    <span class="logo"><span class="dot"></span>Lucid Haven</span>
    <div class="contacts">
      <span><i></i>1234 Central Ave</span><span><i></i>000-000-0000</span>
      <span>Your City, ST 45608</span><span><i></i>000-000-0000</span>
    </div>
    <div class="band">
      <span class="seg-pink" style="width:58%">www.yourwebsite.com</span>
      <span class="seg-purple" style="width:42%">mail@yourwebsite.com</span>
    </div>
  </section>

  <section class="sheet card card-black"><span class="logo pink"><span class="dot"></span>Lucid Haven</span></section>
  <section class="sheet card card-white"><span class="logo"><span class="dot"></span>Lucid Haven</span></section>

  <!-- CD -->
  <div class="label" style="left:789px;top:560px">CD</div>
  <svg class="abs cd" viewBox="0 0 140 140" aria-hidden="true">
    <circle cx="70" cy="70" r="70" fill="var(--pink)"/>
    <path d="M38 8 C10 40 18 100 40 134 C30 100 26 40 44 6 Z" fill="#fff"/>
    <path d="M104 6 C128 40 126 100 100 134 C116 100 120 40 98 4 Z" fill="#fff"/>
    <circle cx="70" cy="70" r="26" fill="var(--purple)"/>
    <circle cx="70" cy="70" r="13" fill="#c9c9c9"/>
    <circle cx="70" cy="70" r="5" fill="#fff"/>
  </svg>
  <div class="abs cd-label"><span class="logo white"><span class="dot"></span>Lucid Haven</span></div>

  <!-- CD cover -->
  <div class="label" style="left:926px;top:542px">CD_Cover</div>
  <section class="abs cd-cover">
    <div class="tab"></div>
    <div class="body">
      <span class="logo" style="top:76px"><span class="dot"></span>Lucid Haven</span>
      <div class="band">
        <span class="seg-purple" style="width:51%"></span>
        <span class="seg-pink" style="width:49%"></span>
      </div>
    </div>
  </section>

</div>
</body>
</html>
```